Psychotherapy Website - Based in London

I am a newly trained psychotherapist and need a new website for www.delphinecarrow.co.uk.

I offer therapy for addiction, relationships, trauma and many other issues people face in their lives.

I want the website to be welcoming, gentle, feminine and for people to feel safe.

I do not like a page site that scrolls through sections, rather each page should be separate. Here some examples that i like. Sectional rather than scrolled.

https://www.maribethvane.com/
https://www.thequietrooms.com/

The imagery should be around pink using the flower in the logo / wording and around the site:

Here is a link to the flower for ideas:
https://www.lookfindo.com/search?q=pink+gerbera

DelphineCarrow
Compassionate Psychotherapy

Is the logo and subheader for the website. Please use a typeface for the name that is appealing and professional.

Type face similar NOT EXLUSIVLY - JUST AN IDEA like this:
https://glowpostureclub.com/

Basic business card i created as a rough idea below.

I have also added the website copy.

The headers are

Homepage
About Me
Therapy
Common Questions
Blog
Contact Me

Target Market(s)

Clients who are dealing with stress, trauma, pain, addiction

Industry/Entity Type

Therapy and Psychology

Coding

Coded - Design and coding required

Number of Pages Required

5+ page

Font styles to use
Serif
Sans Serif
Script

Colors
0054AA
0677BA
7BADD7
CADEEF
E8F1F8
0094D4
00A9DD
6FCCEA
C7EBF8
E9F6FB
E54698
E96AAD
F1A4CE
F9D9EA
FCEFF6

Requirements
Must have
• Pink Gerbera Flower integrated into design
Nice to have
• Images but not to stock imagery. Needs to look authentic and natural
Should not have
• Stock images of people. Images are important but needs to feel REAL

```html
<!DOCTYPE html>
<html lang="en">
<head>
<meta charset="utf-8">
<title>Delphine Carrow – Compassionate Psychotherapy</title>
<link rel="stylesheet" href="https://fonts.googleapis.com/css2?family=Prata&family=Playfair+Display:wght@400&family=Lora:wght@400&family=Open+Sans:wght@400;600;700&display=swap">
<style>
:root{
  --pink:#e54698;
  --pink-mid:#e96aad;
  --pink-soft:#f1a4ce;
  --pink-pale:#f9d9ea;
  --pink-mist:#fceff6;
  --ink:#111111;
  --white:#ffffff;
  --flower:#c42a78;
}
*{margin:0;padding:0;box-sizing:border-box}
html,body{width:904px;height:1200px;overflow:hidden;background:var(--white)}
body{position:relative;font-family:"Open Sans",sans-serif;color:var(--ink)}
.abs{position:absolute}

/* hero */
.hero{left:0;top:0;width:904px;height:418px;
  background:
   radial-gradient(ellipse at 20% 25%,rgba(214,190,60,.75),transparent 45%),
   radial-gradient(ellipse at 75% 20%,rgba(200,120,50,.6),transparent 50%),
   linear-gradient(180deg,#6a5a3a 0%,#9a6a32 30%,#6b3f22 55%,#3e2a1c 80%,#2a1e16 100%);}
.brand{display:flex;align-items:center}
.brand-mark{width:50px;height:50px;border-radius:50%;background:var(--flower);flex:none}
.brand-text{margin-left:4px}
.brand-name{font-family:"Lora",serif;font-size:20px;line-height:1;padding-bottom:5px;border-bottom:1px solid var(--pink-soft)}
.brand-sub{font-size:9.6px;letter-spacing:.2px;margin-top:4px}
.brand-header{left:117px;top:23px;color:var(--white)}
.brand-footer{left:347px;top:1007px;color:var(--ink)}
.brand-footer .brand-name{border-bottom-color:#c9c9c9}
.nav{left:379px;top:39px;display:flex;gap:15.5px;font-size:10.5px;color:var(--white)}
.btn-pill{display:flex;align-items:center;justify-content:center;border-radius:20px;background:var(--pink-pale);color:var(--pink);font-size:10.5px}
.nav-contact{left:694px;top:33px;width:88px;height:28px}
.hero-title{left:110px;top:158px;width:684px;text-align:center;font-family:"Playfair Display",serif;font-weight:400;font-size:28px;line-height:37px;color:var(--white)}
.hero-btn{left:397px;top:289px;width:110px;height:35px;border:1px solid var(--white);border-radius:20px;color:var(--white);font-size:12.5px;display:flex;align-items:center;justify-content:center;letter-spacing:.3px}

/* about */
.divider{left:409px;top:481px;width:85px;height:1px;background:#9aa0a8}
.divider-flower{left:433px;top:463px;width:38px;height:19px;border-radius:19px 19px 0 0;background:var(--flower)}
.about-title{left:0;top:492px;width:904px;text-align:center;font-family:"Prata",serif;font-weight:400;font-size:29px;letter-spacing:.3px}
.about-intro{left:0;top:542px;width:904px;text-align:center;font-size:9.6px;line-height:17px;letter-spacing:.5px}
.portrait{left:122px;top:594px;width:289px;height:323px;border:4.5px solid var(--pink-pale);border-radius:11px;overflow:hidden}
.portrait-fill{width:100%;height:100%;border-radius:7px;
  background:linear-gradient(180deg,#f2e4d6 0%,#e9d5c0 50%,#ef7a9e 80%,#ea5f8e 100%)}
.about-copy{left:453px;top:587px;width:330px;font-size:9.6px;line-height:17.2px;letter-spacing:.5px}
.about-copy p+p{margin-top:1.5px}
.about-btn{left:451px;top:885px;width:88px;height:27px}

/* footer */
.footer{left:0;top:930px;width:904px;height:236px;
  background:linear-gradient(180deg,rgba(252,239,246,0) 0%,var(--pink-mist) 35%,#fbe0ee 100%)}
.contact-item{display:flex;gap:9px;align-items:center}
.contact-icon{width:42px;height:42px;border-radius:50%;background:var(--pink-mid);display:flex;align-items:center;justify-content:center;flex:none}
.contact-label{font-weight:700;font-size:11.8px;line-height:15px}
.contact-value{font-size:10.5px;line-height:15.5px}
.bar{left:0;top:1166px;width:904px;height:34px;background:var(--pink)}
.copyright{left:123px;top:1174px;font-size:9.3px;color:var(--white)}
.social{top:1174px;width:19px;height:19px;border:1px solid var(--white);border-radius:50%}
</style>
</head>
<body>

<section class="abs hero" role="img" aria-label="Landscape photograph of mountains and a golden coastline at sunset"></section>

<div class="abs brand brand-header">
  <div class="brand-mark"></div>
  <div class="brand-text">
    <div class="brand-name">Delphine Carrow</div>
    <div class="brand-sub">Compassionate Psychotherapy</div>
  </div>
</div>

<nav class="abs nav">
  <span>Home</span><span>About Me</span><span>Therapy</span><span>Common Questions</span><span>Blog</span>
</nav>
<div class="abs btn-pill nav-contact">Contact Me</div>

<h1 class="abs hero-title">I Offer A Range of Psychotherapeutic Approaches Including Transactional Analysis Psychotherapy And Relational Therapy.</h1>
<div class="abs hero-btn">Contact Me</div>

<div class="abs divider-flower" role="img" aria-label="Pink gerbera flower emblem"></div>
<div class="abs divider"></div>
<h2 class="abs about-title">ABOUT DELPHINE CARROW</h2>
<div class="abs about-intro">
  Taking The First Steps Towards Engaging In Therapy Can Be A Very Personal Journey.<br>
  Whilst, it can be challenging, I will ensure to make this journey as safe and as comfortable for you as possible.
</div>

<div class="abs portrait"><div class="portrait-fill" role="img" aria-label="Portrait photograph of the therapist"></div></div>

<div class="abs about-copy">
  <p>Psychotherapy can help you see your current situation in new light, depth and clarity. It can change old and unhelpful perspectives &amp; feelings about yourself and your life, &amp; ultimately help you make positive changes.? It might be the most important journey you’ll ever make. I provide a and non-judgmental space where any issues can be explored in complete confidentiality.</p>
  <p>My practice is based in Richmond, where the room is homely, comfortable and welcoming. I believe a good environment contributes to great therapy.</p>
  <p>Alternately, I am also available to provide therapy online, if this environment is more accommodating for my clients.</p>
  <p>I am passionate about improving mental health and committed to offering therapy to all individuals regardless of their age, race, culture, disability, sexual orientation, or socio-economic background.</p>
</div>
<div class="abs btn-pill about-btn">Contact Me</div>

<footer class="abs footer" role="img" aria-label="Faint pink-toned landscape photograph behind the contact details"></footer>

<div class="abs brand brand-footer">
  <div class="brand-mark"></div>
  <div class="brand-text">
    <div class="brand-name">Delphine Carrow</div>
    <div class="brand-sub">Compassionate Psychotherapy</div>
  </div>
</div>

<div class="abs contact-item" style="left:122px;top:1083px">
  <div class="contact-icon">
    <svg width="24" height="24" viewBox="0 0 24 24" fill="none" stroke="#fff" stroke-width="1.3">
      <circle cx="11" cy="14" r="7"/><path d="M4 14h14M11 7c-3 4-3 10 0 14M11 7c3 4 3 10 0 14"/>
      <path d="M17 2a3 3 0 0 1 3 3c0 2-3 5-3 5s-3-3-3-5a3 3 0 0 1 3-3z" fill="var(--pink-mid)"/>
    </svg>
  </div>
  <div>
    <div class="contact-label">Address</div>
    <div class="contact-value">42 Willow Lane, Twickenham<br>Middlesex, TW2 5LP</div>
  </div>
</div>

<div class="abs contact-item" style="left:390px;top:1083px">
  <div class="contact-icon">
    <svg width="24" height="24" viewBox="0 0 24 24" fill="none" stroke="#fff" stroke-width="1.4" stroke-linejoin="round">
      <path d="M6 3l3 4-2 2c1 3 4 6 7 7l2-2 4 3-2 3C10 20 4 14 3 6z"/>
      <path d="M14 6a4 4 0 0 1 4 4M14 2a8 8 0 0 1 8 8"/>
    </svg>
  </div>
  <div>
    <div class="contact-label">Phone Number</div>
    <div class="contact-value">020 7946 0183</div>
  </div>
</div>

<div class="abs contact-item" style="left:605px;top:1083px">
  <div class="contact-icon">
    <svg width="24" height="24" viewBox="0 0 24 24" fill="none" stroke="#fff" stroke-width="1.3" stroke-linejoin="round">
      <path d="M3 10l9-7 9 7v11H3z"/><path d="M3 10l9 6 9-6"/><path d="M3 21l7-6M21 21l-7-6"/>
      <path d="M7 5h10v6"/><path d="M9 8h6"/>
    </svg>
  </div>
  <div>
    <div class="contact-label">Email Address</div>
    <div class="contact-value">dc@delphinecarrow.co.uk</div>
  </div>
</div>

<div class="abs bar"></div>
<div class="abs copyright">Copyright © 2021 Delphine Carrow. All Rights Reserved.</div>
<div class="abs social" style="left:740px"></div>
<div class="abs social" style="left:763px"></div>

</body>
</html>
```